Architecture firm needing a business card

We need a business card design for a new company based in the US called "Dorrance Architecture". Seeking minimalist designs that have a creativity/design feel but must be clean and professional. Please refer to the logo attached.

Target Market(s)

Real Estate Investors, Home Builders and Construction Firms.

Industry/Entity Type

Architecture

Contact Information for Business Card

Standard US size business cards. Would like to have some sort of graphic on the back side of the card - nothing that is too loud but something that may catch your attention. More or less grayscale colors that are in line with the logo colors (navy and greys essentially). Additional colors maybe accepted if blended properly (earthtones), but might be difficult to accomplish and maintain the clean/minimalist look.

Requirements
Must have
• Clean Lines
Nice to have
• some sort of graphics, would like to have something creative on the back side of the card
Should not have
• nothing too busy, cluttered or overwhelming.

```html
<!DOCTYPE html>
<html lang="en">
<head>
<meta charset="utf-8">
<title>Dorrance Architecture – Business Card</title>
<link href="https://fonts.googleapis.com/css2?family=Jost:wght@300;400;500&display=swap" rel="stylesheet">
<style>
  :root {
    --navy: #1c3f66;
    --grey: #999a9a;
    --text-grey: #7f8185;
    --paper: #e9eaec;
    --backdrop: #8b8c8c;
    --white: #ffffff;
  }
  * { margin: 0; padding: 0; box-sizing: border-box; }
  html, body { width: 1200px; height: 900px; overflow: hidden; }
  body {
    background: var(--backdrop);
    font-family: "Jost", sans-serif;
    position: relative;
  }
  .card {
    position: absolute;
    left: 345px;
    width: 510px;
    height: 290px;
  }
  .card-front {
    top: 118px;
    background: var(--navy);
    display: flex;
    align-items: center;
    justify-content: center;
  }
  .brand { display: flex; align-items: center; gap: 16px; }
  .brand-square { width: 60px; height: 60px; background: var(--white); }
  .brand-name { color: var(--white); font-weight: 400; line-height: 1; }
  .brand-name .primary { display: block; font-size: 44px; letter-spacing: 1px; }
  .brand-name .secondary { display: block; font-size: 19px; letter-spacing: 4.3px; margin-top: 6px; }

  .card-back { top: 470px; background: var(--paper); }
  .contact {
    position: absolute;
    left: 38px;
    top: 34px;
    width: 162px;
    color: var(--text-grey);
    font-weight: 400;
  }
  .person-name { color: var(--navy); font-size: 21px; font-weight: 400; line-height: 1.1; }
  .person-role { font-size: 14.5px; margin-top: 3px; letter-spacing: 0.3px; }
  .person-email { font-size: 12.5px; margin-top: 3px; letter-spacing: 0.4px; }
  .divider { border: 0; border-top: 1.5px dotted var(--text-grey); margin: 10px 0 12px; }
  .phone-list { list-style: none; font-size: 13.5px; letter-spacing: 0.6px; }
  .phone-list li { display: flex; align-items: center; gap: 7px; height: 20.5px; }
  .phone-list svg { width: 13px; height: 13px; fill: var(--navy); flex: none; }
  .address { font-size: 13.5px; line-height: 16.5px; letter-spacing: 0.4px; margin-top: -1px; }
  .website { color: var(--navy); font-size: 13.5px; letter-spacing: 0.4px; margin-top: 2px; }

  .back-mark {
    position: absolute;
    left: 255px;
    top: 36px;
    width: 223px;
    height: 217px;
    display: flex;
    flex-direction: column;
    align-items: center;
    justify-content: center;
    gap: 22px;
  }
  .back-mark-square { width: 96px; height: 96px; background: var(--grey); }
  .back-mark-name { color: var(--navy); font-size: 34px; font-weight: 400; letter-spacing: 1px; }
</style>
</head>
<body>
  <section class="card card-front" aria-label="Business card front">
    <div class="brand">
      <div class="brand-square"></div>
      <div class="brand-name">
        <span class="primary">DORRANCE</span>
        <span class="secondary">ARCHITECTURE</span>
      </div>
    </div>
  </section>

  <section class="card card-back" aria-label="Business card back">
    <div class="contact">
      <h1 class="person-name">MARA ELLISON</h1>
      <p class="person-role">CEO/FOUNDER</p>
      <p class="person-email">mara@dorrance.co</p>
      <hr class="divider">
      <ul class="phone-list">
        <li>
          <svg viewBox="0 0 16 16" aria-hidden="true"><path d="M3.2 1.5l2.4 2.7-1.3 1.9c.9 2 2.6 3.7 4.6 4.6l1.9-1.3 2.7 2.4-1.4 2.3C7 14 2 9 1 3z"/></svg>
          555 210 4817
        </li>
        <li>
          <svg viewBox="0 0 16 16" aria-hidden="true"><path d="M4 0h8v16H4zM5.5 2v10h5V2zM7 13.2h2v1.3H7z" fill-rule="evenodd"/></svg>
          555 362 0954
        </li>
        <li>
          <svg viewBox="0 0 16 16" aria-hidden="true"><path d="M4 1h8v4H4zM1 6h14v6h-2v-2H3v2H1zM4 11h8v4H4z"/></svg>
          555 748 3126
        </li>
      </ul>
      <hr class="divider">
      <p class="address">4120 Larkspur Court<br>Boise, Idaho 83702</p>
      <p class="website">www.dorrance.co</p>
    </div>
    <div class="back-mark">
      <div class="back-mark-square"></div>
      <span class="back-mark-name">DORRANCE</span>
    </div>
  </section>
</body>
</html>
```